Hotel Newsletter Design

We need 4 newsletter templates for a luxurious hotel. The templates only differ in the headers (basically each has different images based on a certain theme and/or distinguishing colours). Please feel free to use other colour that those on the webpage of the hotel.

Previous newsletters were these:

"Wine bar" - http://www.palemoorinn.example/newsletter.php?id=76&lang=en
"Feast" - http://www.palemoorinn.example/newsletter.php?id=75&lang=en
"Hotel" - http://www.palemoorinn.example/newsletter.php?id=77&lang=en
"Restaurant" - http://www.palemoorinn.example/newsletter.php?id=78&lang=en

These were too basic and old-fashioned, we need something more UP-TO-DATE, FRESH, MORE MODERN DESIGN.

The final newsletter will be an HTML page with an editable section.

So upon designing please pay attention to leave a space for editable content, which is going to be text and images.

Header and footer required, these won't be editable.

The 4 different header themes are Wine bar, Hotel, Feast, Restaurant.

the website of the hotel:
http://www.palemoorinn.example/
images that can be used:
http://www.vrelkopix.example/temp/brana/images.zip

Target Market(s)

Luxurious Hotel Visitors

Industry/Entity Type

Hospitality

Requirements
Must have
• Logo in the header, address and contact in the footer
Nice to have
• Modern design
Should not have
• Old fashioned design

```html
<!DOCTYPE html>
<html lang="en">
<head>
<meta charset="utf-8">
<title>Pale Moor Inn – Newsletter</title>
<link rel="stylesheet" href="https://fonts.googleapis.com/css2?family=Arimo:wght@400;700&family=Cinzel:wght@400;600&family=Caveat:wght@400;600&display=swap">
<style>
:root{
  --paper:#e4d6bb;
  --paper-dark:#d6c4a2;
  --ink:#3a2d22;
  --ink-soft:#5a4836;
  --brand:#b3252c;
  --frame:#fbfaf6;
  --footer:#86bccb;
  --footer-ink:#ffffff;
  --badge:#1d1d1d;
}
*{box-sizing:border-box;margin:0;padding:0}
html,body{width:1200px;height:3927px;overflow:hidden}
body{
  position:relative;
  background:linear-gradient(180deg,var(--paper) 0%,var(--paper-dark) 50%,var(--paper) 100%);
  color:var(--ink);
  font-family:'Arimo',Arial,sans-serif;
  font-size:16px;line-height:23px;
}
.abs{position:absolute}
/* header */
.header{left:0;top:0;width:1200px;height:800px;background:#f1ead9}
.brand{left:40px;top:40px;display:flex;align-items:center;gap:16px}
.brand-dot{width:44px;height:44px;border-radius:50%;background:var(--brand)}
.brand-name{font-family:'Cinzel',serif;font-weight:600;font-size:34px;color:var(--brand);letter-spacing:1px}
.hero{left:330px;top:0;width:870px;height:790px;
  background:linear-gradient(135deg,#6b4a2a 0%,#c9a36c 35%,#efe3c7 60%,#a47b4b 100%)}
.theme-label{left:20px;top:700px;font-family:'Cinzel',serif;font-weight:600;font-size:56px;color:var(--brand)}
.header-rule{left:0;top:790px;width:1200px;height:10px;background:var(--brand)}
/* sections */
.section h2{font-size:17px;font-weight:700;margin-bottom:18px}
.section p{margin-bottom:18px}
.section .right{text-align:right}
.polaroid{background:var(--frame);padding:22px 22px 70px;box-shadow:4px 6px 14px rgba(0,0,0,.35)}
.polaroid .photo{width:100%;height:100%}
.polaroid .caption{position:absolute;bottom:12px;right:26px;font-family:'Caveat',cursive;font-size:40px;color:var(--ink-soft)}
.offers{font-weight:700}
/* footer */
.footer{left:0;top:3775px;width:1200px;height:152px;background:var(--footer);color:var(--footer-ink)}
.footer-address{left:40px;top:40px;font-size:17px;line-height:24px}
.member{right:40px;top:50px;display:flex;align-items:center;gap:14px;font-size:15px;line-height:19px;font-weight:700;color:var(--badge)}
.member-badge{width:50px;height:50px;border-radius:50%;background:var(--badge)}
</style>
</head>
<body>

<header class="abs header">
  <div class="abs hero" role="img" aria-label="Photograph of an elegant hotel bedroom with a white bed and warm lamplight"></div>
  <div class="abs brand"><span class="brand-dot"></span><span class="brand-name">Pale Moor Inn</span></div>
  <div class="abs theme-label">HOTEL</div>
  <div class="abs header-rule"></div>
</header>

<section class="abs section" style="left:80px;top:830px;width:620px">
  <h2 class="right">Seasons Greetings</h2>
  <p>We would like to give heartfelt thanks to all of our friends and partners for their enthusiasm and tremendous support during this past year. It has been a pleasure working with each and every one of you and it's because of you that we can safely say we are where we are today. On behalf of the whole team at Pale Moor Inn, we wish you a Merry Christmas and truly prosperous New Year! May your holiday season be aglow with warmth and filled by those you care about.</p>
  <p class="right">We look forward to seeing all of you in 2010!</p>
  <p class="right">Always at your service,</p>
  <p class="right">Mattias Lohr</p>
</section>
<div class="abs polaroid" style="left:740px;top:790px;width:380px;height:420px;transform:rotate(4deg)">
  <div class="photo" role="img" aria-label="Photograph of red Christmas ornaments on a fir branch" style="background:radial-gradient(circle at 40% 45%,#c0272d 0%,#6b1214 30%,#1f3520 70%,#0e1a0f 100%)"></div>
  <span class="caption">Season greetings</span>
</div>

<div class="abs polaroid" style="left:45px;top:1330px;width:400px;height:460px;transform:rotate(-3deg)">
  <div class="photo" role="img" aria-label="Photograph of a snowy old-town street at dusk" style="background:linear-gradient(180deg,#3c5a86 0%,#8a7a6a 50%,#d9b27a 80%,#efe7da 100%)"></div>
  <span class="caption">White Day</span>
</div>
<section class="abs section" style="left:545px;top:1345px;width:610px">
  <h2>White days in Tallinn</h2>
  <p>The medieval Tallinn Old Town is a special place no matter what season you happen to be visiting, but it truly sparkles during the colder months. Snow covered cobblestone streets, the warm glow of shop windows and the bustling Christmas market make it a truly magical sight when the mercury drops to a few degrees below zero. If you happen to be planning your trip here during the winter season, we suggest you take advantage of our 'White Days Package', which includes three luxurious nights at our hotel, airport or harbour pick-up and transfer, a 2.5-hour private tour of the city on any day of your choosing and a buffet breakfast, delightfully prepared by our fantastic team at the acclaimed Pale Moor Restaurant. You certainly won't regret a visit to this World Heritage site and we're quite sure you won't be disappointed with the 'white days' or the 'white nights'.</p>
</section>

<section class="abs section" style="left:80px;top:1905px;width:620px">
  <h2 class="right">New Year's Eve</h2>
  <p>What could be better than spending New Year's Eve in the intimate, history-filled ambiance of Pale Moor Inn. We dare to say "Nothing could be better".</p>
  <p>Our 'New Year's Eve Package' includes, three wonderful nights of accommodation, airport or harbour pick-up and transfer in our personal shuttle, a 2.5-hour private, guided tour of the Old Town, a sumptuous 7-course New Year's Eve dinner with corresponding wines and 4.5 hours of savvy pampering at the famous Relax Spa. For just a taste of what you can expect, please see our full New Year's Eve menu.</p>
  <p>If you're going to ring in the New Year or say goodbye to the Old Year in Tallinn, our team of professionals will take care of all the arrangements for you. To turn your celebrations into a memory that will last a lifetime, Pale Moor Inn is at your beck and call.</p>
</section>
<div class="abs polaroid" style="left:745px;top:1945px;width:380px;height:430px;transform:rotate(3deg)">
  <div class="photo" role="img" aria-label="Photograph of two champagne glasses with sparkling lights" style="background:radial-gradient(circle at 50% 55%,#f3dc8a 0%,#b98a2c 30%,#2a1c0c 70%,#0c0905 100%)"></div>
  <span class="caption">New Year Eve!!</span>
</div>

<div class="abs polaroid" style="left:45px;top:2530px;width:400px;height:450px;transform:rotate(-3deg)">
  <div class="photo" role="img" aria-label="Photograph of a set dining table with white tablecloths" style="background:linear-gradient(160deg,#7a2a22 0%,#c98e6a 40%,#f4ede2 75%,#d6c9b5 100%)"></div>
  <span class="caption">Food &amp; Beverage</span>
</div>
<section class="abs section" style="left:545px;top:2550px;width:610px">
  <h2>Food &amp; Beverage service</h2>
  <p>If you've ever dreamed of hosting a dinner party in your own home, but find the task of preparing a culinary work of art to serve to your guests more than a little daunting, we can help. Our highly trained gurus of the culinary arts will assist you in conceiving, preparing and selecting the perfect corresponding wines to accompany a meal that's fit for royalty. In fact the only thing we don't do is the dishes. Whether it be Christmas goose or a New Year's eel supper, we will prepare an edible experience that will leave your guests speechless and don't worry, we won't tell them that we did it for you.</p>
</section>

<section class="abs section" style="left:80px;top:3060px;width:620px">
  <h2>News from Silkline House</h2>
  <p>December is a month of celebrations, Christmas, New Year's Eve...</p>
  <p>In addition to spending quality time with our loved ones, we all have also several festive events to attend. In order to help you look your best, Silkline House is delighted to provide you with the following special offers in December.</p>
  <div class="offers" style="margin-top:30px">
    <p style="margin-bottom:18px">For Men:</p>
    <p>Varnelli 2+1-2 Varnelli suits with a price of 1</p>
    <p>Lumeret -50%</p>
    <p>VRL -50%</p>
  </div>
</section>

<footer class="abs footer">
  <div class="abs footer-address">Pale Moor Inn, Moor Lane 8, Tallinn 10990 Estonia<br>Tel +372 600 0100 Fax 600 0101<br>Email: info@palemoorinn.example</div>
  <div class="abs member"><span class="member-badge"></span><span>A MEMBER OF<br>VESTERBAY HOTELS</span></div>
</footer>

</body>
</html>
```